I need the Scorecard I've developed for my staff to be produced into a visually engaging piece that will encourage the staff to utilize it on a daily basis. I'm thinking it could be 5x7 in size so that it isn't too cumbersome, but I'm open to different layouts.
I have multiple other departments that will need Scorecards created for them as well, but each one will contain task specific questions for each department.

```html
<!DOCTYPE html>
<html lang="en">
<head>
<meta charset="utf-8">
<title>Receptionist Daily Excellence Scorecard</title>
<link rel="stylesheet" href="https://fonts.googleapis.com/css2?family=Fredoka:wght@500;600&family=Nunito:wght@600;700;800&family=Open+Sans:wght@400;600;700&display=swap">
<style>
:root{
  --ink:#000;
  --charcoal:#444;
  --paper:#fff;
  --canvas-top:#fff;
  --canvas-bottom:#f2f2f2;
  --soft:#f4f4f4;
  --line:#d9d9d9;
  --muted:#555;
  --dot:#666;
}
*{box-sizing:border-box;margin:0;padding:0}
html,body{width:1200px;height:3143px;overflow:hidden}
body{background:linear-gradient(var(--canvas-top) 0 2400px,var(--canvas-bottom) 2400px);font-family:"Nunito",sans-serif;color:var(--ink);position:relative}
.sheet{position:absolute;left:82px;width:1037px;height:1451px;background:var(--paper);box-shadow:0 6px 18px rgba(0,0,0,.22)}
.sheet-front{top:84px}
.sheet-back{top:1610px;background:var(--ink)}

/* header */
.masthead{height:203px;background:var(--ink);color:var(--paper);text-align:center;position:relative}
.stars{position:absolute;top:26px;left:0;right:0;display:flex;justify-content:center;gap:8px}
.stars svg{width:30px;height:30px;fill:var(--paper)}
.title{position:absolute;top:62px;left:0;right:0;font-family:"Fredoka",sans-serif;font-weight:600;font-size:35px;letter-spacing:.5px}
.id-bar{position:absolute;left:102px;top:126px;width:832px;height:51px;background:var(--paper);border-radius:14px;display:flex;align-items:center;padding:0 26px;gap:38px;color:var(--ink);font-family:"Open Sans",sans-serif;font-size:16px}
.id-field{display:flex;align-items:flex-end;gap:4px}
.field-line{display:inline-block;width:172px;border-bottom:1px solid #bbb;height:16px}
.instructions{position:absolute;top:216px;left:0;right:0;text-align:center;font-family:"Open Sans",sans-serif;font-style:italic;font-size:16px;color:#222}

/* task cards */
.card{position:absolute;width:289px;height:537px;border:2px solid var(--ink);border-radius:24px;background:var(--paper)}
.card .rating-col{position:absolute;right:-2px;top:89px;bottom:-2px;width:97px;background:var(--ink);border-radius:0 0 24px 0}
.card.alt .rating-col{background:var(--charcoal)}
.rating-col .rating-head{color:var(--paper);font-size:13px;font-weight:800;line-height:1.05;padding:6px 8px}
.rating-col .rating-head small{display:block;font-size:11px}
.badge{position:absolute;top:-21px;left:50%;width:40px;height:40px;margin-left:-20px;transform:rotate(45deg);background:var(--paper);border:2px solid var(--ink);border-radius:6px}
.badge svg{position:absolute;left:8px;top:8px;width:22px;height:22px;transform:rotate(-45deg)}
.card-title{position:absolute;left:24px;top:20px;width:236px;height:60px;border-radius:16px;background:var(--ink);color:var(--paper);font-family:"Fredoka",sans-serif;font-weight:500;font-size:19.5px;line-height:1.2;display:flex;align-items:center;justify-content:center;text-align:center}
.card.alt .card-title{background:var(--charcoal)}
.task-label{position:absolute;left:24px;top:110px;font-size:13px;font-weight:700}
.tasks{position:absolute;left:9px;top:136px;width:272px;display:flex;flex-direction:column;gap:14px}
.tasks.tight{gap:8px;top:128px}
.task{position:relative;height:86px;background:var(--paper);border:1px solid var(--line);border-radius:9px;box-shadow:0 1px 3px rgba(0,0,0,.12)}
.tasks.tight .task{height:74px}
.task .what{position:absolute;left:15px;top:10px;width:160px;font-size:13.5px;font-weight:800;line-height:1.25}
.task .divider{position:absolute;left:185px;top:10px;height:32px;border-left:1px solid #bbb}
.task .notes{position:absolute;left:15px;bottom:10px;font-size:13px;color:var(--muted);font-weight:600}

/* back sheet */
.panel{position:absolute;left:59px;top:55px;width:921px;height:1396px;background:var(--paper);border-radius:54px 54px 0 0;overflow:hidden;font-family:"Open Sans",sans-serif}
.status-heading{position:absolute;top:36px;left:0;right:0;text-align:center;font-weight:700;font-size:32px}
.status-heading span{display:inline-block;border-bottom:3px solid #ccc;padding-bottom:2px}
.status-list{position:absolute;left:68px;top:98px;list-style:none}
.status-list li{display:flex;align-items:center;gap:16px;font-size:24px;height:35.5px}
.status-list li i{width:21px;height:21px;border-radius:50%;background:var(--dot)}
.status-list li.mid i{background:#222}
.reflection-band{position:absolute;left:0;right:0;top:284px;height:395px;background:var(--soft)}
.reflection-pill{position:absolute;left:305px;top:254px;width:309px;height:55px;background:var(--ink);color:var(--paper);border-radius:14px;display:flex;align-items:center;justify-content:center;gap:10px;font-weight:700;font-size:29px}
.reflection-pill svg{width:32px;height:32px}
.question{position:absolute;left:87px;font-size:23px;line-height:32px;color:#222}
.answer{position:absolute;left:87px;width:746px;height:52px;background:var(--paper);border-radius:26px}
.section-rule{position:absolute;left:68px;top:720px;width:783px;border-top:2px solid #ccc}
.sf-heading{position:absolute;top:766px;left:0;right:0;text-align:center;font-weight:700;font-size:23px;color:#333}
.sf-heading .muted{color:var(--muted)}
.sf-heading svg{width:22px;height:22px;vertical-align:-3px;margin:0 4px}
.sup-box{position:absolute;left:68px;width:783px;height:120px;border:2px solid #ccc;border-radius:14px}
.box-label{position:absolute;left:20px;top:14px;font-weight:700;font-size:21px;display:flex;align-items:center;gap:8px}
.box-label svg{width:22px;height:22px}
.overall{position:absolute;left:91px;top:1117px}
.overall h3{font-size:26px;font-weight:700;color:#222}
.overall p{font-size:13px;color:#444;margin-top:4px}
.overall-box{position:absolute;left:492px;top:1101px;width:334px;height:68px;border:2px solid #bbb;border-radius:16px}
.sig{position:absolute;font-size:16px;display:flex;align-items:flex-end;gap:6px;color:#222}
.sig .line{display:inline-block;width:172px;border-bottom:1px solid #aaa;height:16px}
</style>
</head>
<body>

<section class="sheet sheet-front">
  <header class="masthead">
    <div class="stars">
      <svg viewBox="0 0 24 24"><path d="M12 2l3 6.6 7.2.8-5.4 4.9 1.5 7.1L12 17.8 5.7 21.4l1.5-7.1L1.8 9.4 9 8.6z"/></svg>
      <svg viewBox="0 0 24 24"><path d="M12 2l3 6.6 7.2.8-5.4 4.9 1.5 7.1L12 17.8 5.7 21.4l1.5-7.1L1.8 9.4 9 8.6z"/></svg>
      <svg viewBox="0 0 24 24"><path d="M12 2l3 6.6 7.2.8-5.4 4.9 1.5 7.1L12 17.8 5.7 21.4l1.5-7.1L1.8 9.4 9 8.6z"/></svg>
      <svg viewBox="0 0 24 24"><path d="M12 2l3 6.6 7.2.8-5.4 4.9 1.5 7.1L12 17.8 5.7 21.4l1.5-7.1L1.8 9.4 9 8.6z"/></svg>
      <svg viewBox="0 0 24 24"><path d="M12 2l3 6.6 7.2.8-5.4 4.9 1.5 7.1L12 17.8 5.7 21.4l1.5-7.1L1.8 9.4 9 8.6z"/></svg>
    </div>
    <h1 class="title">Receptionist Daily Excellence Scorecard</h1>
    <div class="id-bar">
      <div class="id-field">Name: <span class="field-line"></span></div>
      <div class="id-field">Date: <span class="field-line"></span></div>
      <div class="id-field">Location: <span class="field-line"></span></div>
    </div>
  </header>
  <p class="instructions">(Please rate yourself for each task: 1 = Needs Improvement, 3 = Meets Expectations, 5 = Excellent)</p>

  <article class="card" style="left:52px;top:290px">
    <div class="rating-col"><div class="rating-head">Self-Rating<small>(1-5)</small></div></div>
    <div class="badge"><svg viewBox="0 0 24 24"><circle cx="12" cy="9" r="4"/><path d="M5 9a7 7 0 0114 0v3h-2V9a5 5 0 00-10 0v3H5z"/><path d="M5 22c0-4 3-6 7-6s7 2 7 6z"/></svg></div>
    <h2 class="card-title">Call Handling &amp;<br>First Call Intake</h2>
    <span class="task-label">Task:</span>
    <div class="tasks">
      <div class="task"><p class="what">Answered 90%+ calls within 3 rings</p><span class="divider"></span><p class="notes">Notes / Issues:</p></div>
      <div class="task"><p class="what">Maintained empathy and professionalism</p><span class="divider"></span><p class="notes">Notes / Issues:</p></div>
      <div class="task"><p class="what">Accurately completed all First Call fields</p><span class="divider"></span><p class="notes">Notes / Issues:</p></div>
      <div class="task"><p class="what">Worked within Receptionist role</p><span class="divider"></span><p class="notes">Notes / Issues:</p></div>
    </div>
  </article>

  <article class="card alt" style="left:372px;top:290px">
    <div class="rating-col"><div class="rating-head">Self-Rating<small>(1-5)</small></div></div>
    <div class="badge"><svg viewBox="0 0 24 24"><path d="M6.6 10.8a15 15 0 006.6 6.6l2.2-2.2a1 1 0 011-.3 11 11 0 003.5.6 1 1 0 011 1V20a1 1 0 01-1 1A17 17 0 013 4a1 1 0 011-1h3.5a1 1 0 011 1 11 11 0 00.6 3.5 1 1 0 01-.3 1z"/></svg></div>
    <h2 class="card-title">Call Management<br>During Busy Times</h2>
    <span class="task-label">Task:</span>
    <div class="tasks">
      <div class="task"><p class="what">Prioritized urgent vs. non-urgent calls</p><span class="divider"></span><p class="notes">Notes / Issues:</p></div>
      <div class="task"><p class="what">Hold times under minute 1</p><span class="divider"></span><p class="notes">Notes / Issues:</p></div>
      <div class="task"><p class="what">Logged all calls</p><span class="divider"></span><p class="notes">Notes / Issues:</p></div>
      <div class="task"><p class="what">Requested help if overwhelmed</p><span class="divider"></span><p class="notes">Notes / Issues:</p></div>
    </div>
  </article>

  <article class="card" style="left:696px;top:290px">
    <div class="rating-col"><div class="rating-head">Self-Rating<small>(1-5)</small></div></div>
    <div class="badge"><svg viewBox="0 0 24 24"><rect x="3" y="5" width="16" height="15" rx="2"/><rect x="5" y="10" width="12" height="8" fill="#fff"/><rect x="6" y="2" width="2" height="5"/><rect x="14" y="2" width="2" height="5"/><circle cx="19" cy="18" r="4" stroke="#fff" stroke-width="1.5"/></svg></div>
    <h2 class="card-title">Scheduling Accuracy</h2>
    <span class="task-label">Task:</span>
    <div class="tasks">
      <div class="task"><p class="what">Updated scheduling board</p><span class="divider"></span><p class="notes">Notes / Issues:</p></div>
      <div class="task"><p class="what">Cross-checked with Red Book</p><span class="divider"></span><p class="notes">Notes / Issues:</p></div>
      <div class="task"><p class="what">Entered manifold info promptly</p><span class="divider"></span><p class="notes">Notes / Issues:</p></div>
    </div>
  </article>

  <article class="card alt" style="left:52px;top:876px">
    <div class="rating-col" style="top:84px"><div class="rating-head">Self-Rating<small>(1-5)</small></div></div>
    <div class="badge"><svg viewBox="0 0 24 24" fill="none" stroke="#000" stroke-width="1.8"><path d="M12 4c-2 3-2 8 0 12 2-4 2-9 0-12z"/><path d="M12 16c-3-1-6-4-7-8 3 0 6 3 7 8z"/><path d="M12 16c3-1 6-4 7-8-3 0-6 3-7 8z"/><path d="M4 18h16"/></svg></div>
    <h2 class="card-title">Clothing &amp; Flowers</h2>
    <span class="task-label" style="top:102px">Task:</span>
    <div class="tasks tight">
      <div class="task"><p class="what">Clothing sheet completed</p><span class="divider"></span><p class="notes">Notes / Issues:</p></div>
      <div class="task"><p class="what">Family contact noted on sheet</p><span class="divider"></span><p class="notes">Notes / Issues:</p></div>
      <div class="task"><p class="what">Floral deliveries logged</p><span class="divider"></span><p class="notes">Notes / Issues:</p></div>
      <div class="task"><p class="what">Concerns communicated to Care Center</p><span class="divider"></span><p class="notes">Notes / Issues:</p></div>
      <div class="task"><p class="what">Flower placement verified</p><span class="divider"></span><p class="notes">Notes / Issues:</p></div>
    </div>
  </article>

  <article class="card" style="left:372px;top:876px">
    <div class="rating-col"><div class="rating-head">Self-Rating<small>(1-5)</small></div></div>
    <div class="badge"><svg viewBox="0 0 24 24"><path d="M5 2h10l4 4v16H5z"/><rect x="11" y="7" width="2" height="6" fill="#fff"/><rect x="11" y="15" width="2" height="2" fill="#fff"/></svg></div>
    <h2 class="card-title">Death Certificates</h2>
    <span class="task-label">Task:</span>
    <div class="tasks">
      <div class="task"><p class="what">Verified recipient ID &amp; relationship</p><span class="divider"></span><p class="notes">Notes / Issues:</p></div>
      <div class="task"><p class="what">Confirmed correct documents enclosed</p><span class="divider"></span><p class="notes">Notes / Issues:</p></div>
      <div class="task"><p class="what">Recipient signed the DC logbook</p><span class="divider"></span><p class="notes">Notes / Issues:</p></div>
      <div class="task"><p class="what">Suggested proofreading before leaving</p><span class="divider"></span><p class="notes">Notes / Issues:</p></div>
    </div>
  </article>

  <article class="card alt" style="left:696px;top:876px">
    <div class="rating-col"><div class="rating-head">Self-Rating<small>(1-5)</small></div></div>
    <div class="badge"><svg viewBox="0 0 24 24"><path d="M2 3h14v10H7l-5 4z"/><path d="M18 7h4v14l-4-3H9v-3h9z"/></svg></div>
    <h2 class="card-title">Routing &amp; Messages</h2>
    <span class="task-label">Task:</span>
    <div class="tasks">
      <div class="task"><p class="what">Calls routed appropriately</p><span class="divider"></span><p class="notes">Notes / Issues:</p></div>
      <div class="task"><p class="what">Messages included all required info</p><span class="divider"></span><p class="notes">Notes / Issues:</p></div>
      <div class="task"><p class="what">+Delivered 95% messages in 30 min</p><span class="divider"></span><p class="notes">Notes / Issues:</p></div>
    </div>
  </article>
</section>

<section class="sheet sheet-back">
  <div class="panel">
    <h2 class="status-heading"><span>Daily Status Summary (Circle One)</span></h2>
    <ul class="status-list">
      <li><i></i>Excellent – All key duties completed, proactive, calm under pressure</li>
      <li class="mid"><i></i>Satisfactory – Most duties completed, minor follow-up needed</li>
      <li><i></i>Needs Support – Missed urgent duties, accuracy or stress issues</li>
    </ul>

    <div class="reflection-band"></div>
    <div class="reflection-pill">
      <svg viewBox="0 0 24 24" fill="none" stroke="#fff" stroke-width="2"><path d="M4 12a8 8 0 108-8 8 8 0 00-6 2.7"/><path d="M4 3v4h4"/><path d="M12 8v4l3 2"/></svg>
      Daily Reflection
    </div>
    <p class="question" style="top:334px">What went well today?</p>
    <div class="answer" style="top:376px"></div>
    <p class="question" style="top:444px">Any issues or barriers to note?</p>
    <div class="answer" style="top:486px"></div>
    <p class="question" style="top:554px">Support needed from supervisor?</p>
    <div class="answer" style="top:596px"></div>

    <div class="section-rule"></div>
    <h3 class="sf-heading"><svg viewBox="0 0 24 24" fill="#999"><path d="M9 3l2 6 6 2-6 2-2 6-2-6-6-2 6-2z"/><path d="M18 2l1 3 3 1-3 1-1 3-1-3-3-1 3-1z"/></svg>Stars &amp;<svg viewBox="0 0 24 24" fill="#777"><rect x="4" y="3" width="2" height="19"/><path d="M6 4h13l-3 4 3 4H6z"/></svg>Flags (<span class="muted">Supervisor Use Only</span>)</h3>
    <div class="sup-box" style="top:826px">
      <p class="box-label"><svg viewBox="0 0 24 24" fill="#999"><path d="M9 3l2 6 6 2-6 2-2 6-2-6-6-2 6-2z"/><path d="M18 2l1 3 3 1-3 1-1 3-1-3-3-1 3-1z"/></svg>Stars (Excellence or above-and-beyond moments):</p>
    </div>
    <div class="sup-box" style="top:962px">
      <p class="box-label"><svg viewBox="0 0 24 24" fill="#777"><rect x="4" y="3" width="2" height="19"/><path d="M6 4h13l-3 4 3 4H6z"/></svg>Flags (Concerns needing follow-up/coaching):</p>
    </div>

    <div class="overall">
      <h3>Manager Overall Rating (1-5):</h3>
      <p>(Manager: Please rate overall performance on a 1-5 scale)</p>
    </div>
    <div class="overall-box"></div>

    <p class="sig" style="left:89px;top:1250px">Receptionist Signature: <span class="line"></span></p>
    <p class="sig" style="left:486px;top:1250px">Supervisor Signature: <span class="line"></span></p>
    <p class="sig" style="left:347px;top:1299px">Date: <span class="line"></span></p>
  </div>
</section>

</body>
</html>
```